Letterhead design for business

Looking for an attractive and professional letterhead that uses the logo that is attached below.

Target Market(s)

Potential bankruptcy clients.

Industry/Entity Type

Legal

Colors

Designer to choose colors to be used in the design.

Requirements
Must have
• Address for locations, phone number, and website address.
• Addresses are on website ferncoveadvice.example. Use following phone number (for tracking purposes): 555-013-8274

```html
<!DOCTYPE html>
<html lang="en">
<head>
<meta charset="utf-8">
<title>Fern Cove Law Group – Letterhead</title>
<link href="https://fonts.googleapis.com/css2?family=Roboto:wght@400;500&display=swap" rel="stylesheet">
<style>
  :root {
    --backdrop: #cfcfd3;
    --paper: #ffffff;
    --brand-green: #8ec585;
    --brand-green-dark: #6fae66;
    --ink: #3a3a3a;
    --ink-soft: #6a6a6a;
  }
  * { margin: 0; padding: 0; box-sizing: border-box; }
  html, body {
    width: 1200px; height: 878px; overflow: hidden;
    background: var(--backdrop);
    font-family: "Roboto", Arial, sans-serif;
  }
  .canvas { position: relative; width: 1200px; height: 878px; }

  .sheet {
    position: absolute; top: 128px; width: 476px; height: 614px;
    background: var(--paper);
  }
  .sheet--front { left: 106px; border-top: 5px solid var(--brand-green); }
  .sheet--back { left: 630px; background: var(--brand-green); }

  .brand { position: absolute; left: 44px; top: 56px; display: flex; align-items: center; gap: 10px; }
  .brand__mark { width: 44px; height: 44px; border-radius: 50%; background: var(--brand-green); }
  .brand__name { font-size: 22px; font-weight: 500; color: var(--brand-green-dark); letter-spacing: 0.2px; }
  .brand__tagline { position: absolute; left: 98px; top: 108px; font-size: 7px; color: var(--brand-green-dark); }

  .contact {
    position: absolute; right: 380px; top: 176px; width: 100px;
    text-align: right; font-size: 6px; line-height: 8.4px; color: var(--ink-soft);
  }
  .contact__office { margin-bottom: 16px; }
  .contact__label { color: var(--brand-green-dark); }

  .letter {
    position: absolute; left: 128px; top: 176px; width: 316px;
    font-size: 7px; line-height: 9.3px; color: var(--ink-soft); text-align: justify;
  }
  .letter p { margin-bottom: 9px; }
  .letter__closing { margin-top: 24px; }
  .letter__signoff { display: flex; align-items: flex-end; gap: 12px; margin-top: 8px; }
  .letter__name { color: var(--ink); }
  .letter__signature { width: 80px; height: 30px; background: linear-gradient(90deg, #f1f1f1, #e6e6e6); }

  .website {
    position: absolute; left: 38px; bottom: 20px;
    font-size: 6.5px; letter-spacing: 0.6px; color: var(--brand-green-dark); font-weight: 500;
  }
</style>
</head>
<body>
<main class="canvas">
  <section class="sheet sheet--front">
    <div class="brand">
      <span class="brand__mark"></span>
      <span class="brand__name">Fern Cove Law Group</span>
    </div>
    <div class="brand__tagline">by Attorney R. Lindqvist</div>

    <address class="contact">
      <div class="contact__office">418 Linden Row<br>NW Suite #1400<br>Marlow, Georgia 30321</div>
      <div class="contact__office">2915 E. Alder St.<br>Brookhaven Falls<br>Georgia 30187</div>
      <div><span class="contact__label">Tel:</span> 555-013-8274</div>
    </address>

    <article class="letter">
      <p>Dear Mr. Halvorsen:</p>
      <p>As Chairperson of the Corporate Conscience Campaign - Helping the Homeless in New York, I am writing this to thank you personally for your company's support in last month's fund-raising effort.</p>
      <p>As I indicated when we spoke on the phone two weeks ago, the campaign was considered a resounding success, raising a total of $1.65 million to-date, significantly exceeding our target of $1 million. Some donations are still trickling in, so we could end up close to a total of $2 million.</p>
      <p>NorthPeak Labs was an influential leader throughout the entire three-month campaign. In fact, we couldn't have succeeded without the generous support of your company, both financially, and through your organizational and administrative assistance. Your Team Leader, Elena Marsh was particularly impressive, going above and beyond what we could have expected of someone performing as a volunteer while continuing on with her day-to-day duties. Please convey my special thanks to Elena.</p>
      <p>I would also ask you to convey my sincere thanks and congratulations to all of those other people in your company who contributed in any way to the Helping the Homeless Campaign. Please tell them that the sum of their contributions resulted in a major success that they should all be proud of taking part in.</p>
      <p>I believe that the 27 companies that participated in this effort have set a new standard for social responsibility in this community, and have set a powerful example that will inspire other companies and organizations to do the same.</p>
      <p>I look forward to seeing you at the Mayor's special thank you reception next month.</p>
      <div class="letter__closing">Yours sincerely,</div>
      <div class="letter__signoff">
        <div><span class="letter__name">Martin Ellery</span><br>Fundraising Chair</div>
        <div class="letter__signature" role="img" aria-label="Handwritten signature"></div>
      </div>
    </article>

    <div class="website">ferncoveadvice.example</div>
  </section>

  <section class="sheet sheet--back" role="img" aria-label="Green chevron pattern covering the reverse of the letterhead"></section>
</main>
</body>
</html>
```